International Fleet Management Firm Website

HaulwaveKenro is a Fleet Management Company that provides insight into customers fleets. We do this through web tools which we have developed which function through a client login screen to help ensure that corporates are able to stay on top of their fleets 24/7.
We are about to launch and are looking for a great new website to help us come out with bang! We would like a site that matches our values of ; Courage, integrity and leadership.
Although we have developed the app. We would also like to redesign the look of the site on the back end.
(1) We need to incorporate the new corporate colours
(2) Would like to create a better user experience.
The site that I would like to model ours after is;
www.belvanmotors.com (usa version)
Good Luck!!
Updates
Jusst added the .png version of the logo. Hopes this helps!
Industry/Entity Type
It Company
Look and feel

```html
<!DOCTYPE html>
<html lang="en">
<head>
<meta charset="utf-8">
<title>HaulwaveKenro – Drivers</title>
<link href="https://fonts.googleapis.com/css2?family=Source+Sans+3:wght@300;400;600;700&display=swap" rel="stylesheet">
<style>
:root{
  --page-bg:#f4f4f4;
  --white:#ffffff;
  --nav-top:#5ec3ee;
  --nav-bottom:#2c93d2;
  --nav-divider:rgba(255,255,255,0.28);
  --nav-divider-dark:rgba(0,70,130,0.25);
  --brand:#1b8fc9;
  --btn-top:#2a8fcf;
  --btn-bottom:#15609c;
  --text-dark:#555555;
  --text-mid:#666666;
  --text-light:#888888;
  --line:#d6d6d6;
  --line-soft:#e6e6e6;
  --icon-grey:#b9b9b9;
}
*{box-sizing:border-box;margin:0;padding:0}
html,body{width:1200px;height:770px;overflow:hidden}
body{position:relative;background:var(--page-bg);font-family:"Source Sans 3",Arial,sans-serif;color:var(--text-dark)}
.site-header{position:absolute;left:0;top:0;width:1200px;height:111px;background:var(--white)}
.brand{position:absolute;left:88px;top:30px;display:flex;align-items:center;gap:12px}
.brand-mark{width:40px;height:40px;background:var(--brand)}
.brand-name{font-size:32px;font-weight:700;color:var(--brand);letter-spacing:-0.5px}
.header-btn{position:absolute;top:60px;height:35px;border:1px solid #cfcfcf;border-radius:2px;background:linear-gradient(#fbfbfb,#ececec);display:flex;align-items:center;gap:6px;padding:0 12px;font-size:14px;color:var(--text-mid)}
.header-btn strong{font-weight:600;color:#333;margin-left:4px}
.btn-alerts{left:858px;width:104px}
.btn-account{left:976px;width:135px}
.main-nav{position:absolute;left:0;top:111px;width:1200px;height:99px;background:linear-gradient(var(--nav-top),var(--nav-bottom))}
.nav-item{position:absolute;top:0;height:99px;display:flex;flex-direction:column;align-items:center;justify-content:flex-end;padding-bottom:15px;color:var(--white);font-size:19.5px;font-weight:400}
.nav-item svg{margin-bottom:8px}
.nav-item.sep{border-left:1px solid var(--nav-divider-dark);box-shadow:inset 1px 0 0 var(--nav-divider)}
.nav-item.active{background:var(--white);color:var(--brand)}
.active-pointer{position:absolute;left:229px;top:210px;width:115px;height:36px}
.content-panel{position:absolute;left:77px;top:210px;width:1046px;height:451px;background:var(--white)}
.side-title{position:absolute;left:117px;top:278px;font-size:29px;font-weight:300;color:#4a4a4a}
.side-menu{position:absolute;left:116px;top:317px;width:190px;list-style:none;border-top:1px solid #cccccc}
.side-menu li{height:36px;display:flex;align-items:center;justify-content:space-between;font-size:14px;color:var(--text-mid);border-bottom:1px solid #cccccc;padding:0 10px 0 2px}
.side-menu li:last-child{border-bottom:none}
.btn-add{position:absolute;left:350px;top:276px;width:192px;height:33px;border-radius:2px;background:linear-gradient(var(--btn-top),var(--btn-bottom));color:var(--white);font-size:14.5px;font-weight:600;display:flex;align-items:center;gap:8px;padding-left:16px}
.search{position:absolute;left:822px;top:275px;width:273px;height:35px;border:1px solid var(--line);display:flex}
.search span{flex:1;padding-left:12px;display:flex;align-items:center;font-size:13.5px;font-style:italic;color:var(--text-light)}
.search i{width:37px;border-left:1px solid var(--line);display:flex;align-items:center;justify-content:center}
.driver-table{position:absolute;left:348px;top:325px;width:747px;height:250px;border:1px solid #cfcfcf;border-collapse:collapse}
.table-head{height:42px;background:linear-gradient(#fbfbfb,#ececec);border-bottom:1px solid var(--line);position:relative;font-size:15px;color:var(--text-dark)}
.table-row{height:36px;border-bottom:1px solid var(--line-soft);position:relative;font-size:13px;color:var(--text-mid)}
.cell{position:absolute;top:50%;transform:translateY(-50%)}
.site-footer{position:absolute;left:0;top:708px;width:1200px;height:62px;background:var(--white);border-top:1px solid #e2e2e2}
.copyright{position:absolute;left:79px;top:24px;font-size:14px;color:var(--text-mid)}
.page-code{position:absolute;left:1171px;top:37px;font-size:13px;color:#444}
</style>
</head>
<body>
<header class="site-header">
  <div class="brand"><span class="brand-mark"></span><span class="brand-name">HaulwaveKenro</span></div>
  <div class="header-btn btn-alerts">
    <svg width="18" height="18" viewBox="0 0 24 24" fill="none" stroke="#777" stroke-width="1.6"><path d="M6 16V11a6 6 0 0 1 12 0v5l2 2H4z"/><path d="M10 20a2 2 0 0 0 4 0"/></svg>
    Alerts <strong>0</strong>
  </div>
  <div class="header-btn btn-account">
    <svg width="18" height="18" viewBox="0 0 24 24" fill="#777"><circle cx="12" cy="7" r="5"/><path d="M2 23c0-6 4-9 10-9s10 3 10 9z"/></svg>
    You Account
    <svg width="9" height="6" viewBox="0 0 10 6" fill="#666"><path d="M0 0h10L5 6z"/></svg>
  </div>
</header>

<nav class="main-nav">
  <div class="nav-item" style="left:75px;width:154px">
    <svg width="44" height="36" viewBox="0 0 44 36" fill="none" stroke="#fff" stroke-width="3"><path d="M6 32a18 18 0 1 1 32 0z"/><path d="M22 26l-5-9" stroke-linecap="round"/><circle cx="22" cy="26" r="2" fill="#fff"/></svg>
    Dashboard
  </div>
  <div class="nav-item active" style="left:229px;width:115px">
    <svg width="40" height="38" viewBox="0 0 40 38" fill="#1b8fc9"><circle cx="20" cy="10" r="9"/><path d="M2 38c0-11 7-16 18-16s18 5 18 16z"/><path d="M20 22l-2 8 2 4 2-4z" fill="#fff"/></svg>
    Drivers
  </div>
  <div class="nav-item sep" style="left:344px;width:129px">
    <svg width="44" height="34" viewBox="0 0 44 34" fill="#fff"><rect x="14" y="2" width="29" height="22"/><path d="M1 12h11v14H1z"/><circle cx="8" cy="28" r="4" stroke="#3aa3dc" stroke-width="2"/><circle cx="32" cy="28" r="4" stroke="#3aa3dc" stroke-width="2"/></svg>
    Vehicles
  </div>
  <div class="nav-item sep" style="left:473px;width:103px">
    <svg width="32" height="38" viewBox="0 0 32 38" fill="none" stroke="#fff" stroke-width="3"><path d="M4 6h14l10 8v22H4z"/><path d="M16 18c-4 5-4 7 0 9 4-2 4-4 0-9z" fill="#fff" stroke="none"/></svg>
    Fuel
  </div>
  <div class="nav-item sep" style="left:576px;width:104px">
    <svg width="36" height="36" viewBox="0 0 36 36" fill="none" stroke="#fff" stroke-width="6"><circle cx="18" cy="18" r="14"/></svg>
    Tyres
  </div>
  <div class="nav-item sep" style="left:680px;width:107px">
    <svg width="34" height="34" viewBox="0 0 34 34" fill="#fff"><path d="M9 2h16l8 32H1z"/><rect x="15" y="6" width="4" height="6" fill="#3aa3dc"/><rect x="15" y="16" width="4" height="6" fill="#3aa3dc"/><rect x="14" y="26" width="6" height="8" fill="#3aa3dc"/></svg>
    Tasks
  </div>
  <div class="nav-item sep" style="left:787px;width:164px">
    <svg width="36" height="36" viewBox="0 0 36 36" fill="none" stroke="#fff" stroke-width="5" stroke-linecap="round"><path d="M6 30L22 14"/><path d="M30 30L12 12"/><circle cx="26" cy="9" r="5" stroke-width="3"/><path d="M6 6l6 6" stroke-width="6"/></svg>
    Maintenance
  </div>
  <div class="nav-item sep" style="left:951px;width:174px">
    <svg width="38" height="38" viewBox="0 0 38 38" fill="#fff"><path d="M3 2v33h33" fill="none" stroke="#fff" stroke-width="3"/><rect x="9" y="22" width="4" height="10"/><rect x="15" y="16" width="4" height="16"/><rect x="21" y="19" width="4" height="13"/><rect x="27" y="10" width="4" height="22"/></svg>
    Stats &amp; Reports
  </div>
  <div class="nav-item sep" style="left:1125px;width:1px"></div>
</nav>

<main>
  <div class="content-panel"></div>
  <svg class="active-pointer" viewBox="0 0 115 36"><path d="M0 0h115L57.5 36z" fill="#fff"/></svg>

  <h1 class="side-title">Drivers</h1>
  <ul class="side-menu">
    <li>Registered Drivers
      <svg width="20" height="22" viewBox="0 0 20 22" fill="#bcbcbc"><path d="M6 1h3v10h2V7h3v5h2V9h3v8l-3 5H7L2 14l2-2 2 2z"/></svg>
    </li>
    <li>Add New Driver
      <svg width="20" height="22" viewBox="0 0 20 22" fill="#bcbcbc"><circle cx="10" cy="6" r="5"/><path d="M0 22c0-6 4-9 10-9s10 3 10 9z"/></svg>
    </li>
  </ul>

  <div class="btn-add">
    <svg width="18" height="20" viewBox="0 0 20 22" fill="#fff"><circle cx="10" cy="6" r="5"/><path d="M0 22c0-6 4-9 10-9s10 3 10 9z"/></svg>
    Add new dirver details
  </div>

  <div class="search">
    <span>Search here..</span>
    <i><svg width="17" height="17" viewBox="0 0 18 18" fill="none" stroke="#777" stroke-width="2.4"><circle cx="7.5" cy="7.5" r="5.5"/><path d="M12 12l5 5" stroke-linecap="round"/></svg></i>
  </div>

  <div class="driver-table" role="table">
    <div class="table-head" role="row">
      <span class="cell" style="left:28px">Name of Driver</span>
      <span class="cell" style="left:358px">Department</span>
      <span class="cell" style="left:615px">Action</span>
    </div>
    <div class="table-row" role="row">
      <span class="cell" style="left:30px">Duis tincidunt lectus quis dui</span>
      <span class="cell" style="left:361px">Viverra vestibulum.</span>
      <span class="cell" style="left:620px">Invited</span>
    </div>
  </div>
</main>

<footer class="site-footer">
  <p class="copyright">© 2013 Company Name.&nbsp; All right reserved.&nbsp; Term of Use</p>
  <span class="page-code">X14</span>
</footer>
</body>
</html>
```